Coastal Bridge Alliance Web Design

I would like a web design for a conference. Registration, Form completion, Hotel, Speakers etc. See link for sample similar but not the same.
http://kbq-trust.example/pvrlo/index.php/contact-us
We would like the design to depict the colours of the logo which is attached. A banner of the website will be provided. We would like a transitioning space in the top and front page of the website for announcements and showcase of events. We would like custom prepared headers for each grouping, example, Sponsor, Venue, Discussion etc.

```html
<!DOCTYPE html>
<html lang="en">
<head>
<meta charset="utf-8">
<title>Coastal Bridge Alliance Conference 2015</title>
<link rel="stylesheet" href="https://fonts.googleapis.com/css2?family=Open+Sans:ital,wght@0,400;0,600;0,700;1,600&family=Playfair+Display:wght@700&display=swap">
<style>
:root{
  --sky-top:#1690d8;
  --sky-bottom:#cdeaf5;
  --page:#f4f5fa;
  --ink:#111;
  --muted:#666;
  --red:#e5202a;
  --blue:#1b8fd8;
  --blue-dark:#14709f;
  --blue-light:#33ade8;
  --teal:#1fae9a;
  --green:#5c9e2a;
  --nav:#0a0a0a;
}
*{margin:0;padding:0;box-sizing:border-box}
html,body{width:815px;height:1200px;overflow:hidden}
body{position:relative;font-family:"Open Sans",Arial,sans-serif;color:var(--ink);
  background:linear-gradient(180deg,var(--sky-top) 0%,#5fb8e6 45%,var(--sky-bottom) 100%)}
.abs{position:absolute}
.page{left:54px;top:24px;width:707px;height:1126px;background:var(--page)}
.brand{left:78px;top:34px;width:155px;height:61px;background:#fff;display:flex;align-items:center;gap:6px;padding:0 8px}
.brand-dot{width:14px;height:14px;border-radius:50%;background:var(--red);flex:none}
.brand-name{font-size:10px;font-weight:700;color:var(--ink);line-height:1.15}
.tagline{left:347px;top:66px;font-size:9.5px;color:#222}
.tagline em{color:var(--red);font-weight:700}
.nav{left:54px;top:103px;width:707px;height:29px;background:var(--nav);display:flex}
.nav a{color:#fff;text-decoration:none;font-size:7.5px;letter-spacing:.3px;display:flex;align-items:center;justify-content:center;border-right:1px solid #333}
.nav a.active{background:var(--red)}
.slider{left:54px;top:145px;width:707px;height:245px;background:radial-gradient(ellipse at 25% 60%,#1b2540 0%,#2a2432 30%,#6a3a2c 65%,#9a5a3a 100%)}
.slide-title{left:317px;top:214px;font-size:18.5px;font-weight:600;color:#fff;letter-spacing:1.2px}
.slide-by{left:611px;top:259px;font-size:11px;font-weight:600;color:#fff;line-height:18px}
.arrow{top:252px;width:30px;height:30px;background:#d8d8d8;display:flex;align-items:center;justify-content:center}
.welcome{left:88px;top:416px;font-size:19px;font-weight:400}
.welcome span{color:#1e7fc4}
.intro{left:88px;top:454px;width:440px;font-size:7.4px;line-height:18px;color:#555}
.tabs{left:88px;top:526px;height:23px;display:flex;background:var(--blue)}
.tabs span{color:#fff;font-size:8px;font-weight:700;display:flex;align-items:center;padding:0 14px}
.tabs span.on{background:#000;padding:0 16px}
.event-photo{left:88px;width:155px;height:100px}
.event{left:260px;width:213px}
.event h3{font-size:11px;font-weight:700;margin-bottom:3px}
.event p{font-size:7.4px;line-height:17px;color:#666;border-bottom:1px solid #ccc;padding-bottom:4px}
.event .meta{font-size:7px;font-style:italic;font-weight:600;color:#666;margin-top:10px;display:flex;gap:12px;align-items:center}
.meta i{display:inline-block;width:6px;height:6px;background:var(--red);margin-right:5px;border-radius:1px}
.meta i.clock{border-radius:50%}
.pager{left:88px;top:943px;display:flex;gap:6px}
.pager span{width:19px;height:16px;border:1.5px solid #999;font-size:8px;display:flex;align-items:center;justify-content:center;color:#555;font-weight:600}
.pager span.on{border-color:var(--blue);color:var(--blue-dark)}
.promo{left:550px;top:427px;width:175px;height:271px;background:var(--blue)}
.promo-head{height:35px;background:var(--blue-dark);color:#fff;font-family:"Playfair Display",serif;font-size:11.5px;display:flex;align-items:center;justify-content:center}
.promo-card{left:570px;top:470px;width:135px;height:175px;background:var(--blue-light);text-align:center;color:#fff}
.promo-card h4{font-size:11px;font-weight:700;margin:12px 0 0 22px}
.badge{width:76px;height:76px;border-radius:50%;background:#e6f2ea;border:3px solid #2a6a4a;margin:6px auto 6px}
.promo-card p{font-size:7.4px;line-height:14px;padding:0 8px}
.promo-foot{left:550px;top:655px;width:175px;text-align:center;color:#fff}
.promo-foot b{display:block;font-size:9.5px}
.promo-foot span{font-family:"Playfair Display",serif;font-size:8.5px}
.weather{left:550px;top:721px;width:175px;height:200px;border:2px solid #9ec3e0;background:#dde3ee;padding:4px}
.weather-head{height:38px;background:linear-gradient(#1b8fd8,#1676b8);color:#fff;font-size:11px;font-weight:600;display:flex;align-items:center;padding-left:10px}
.weather-body{padding:10px 11px;font-size:7.3px;line-height:14.5px;color:#444}
.weather-body b{font-size:9.5px;color:#555;display:block;margin-bottom:1px}
.temp{left:570px;top:868px;font-size:21px;font-weight:700;color:#e1141e}
.card{top:986px;width:227px;height:148px;color:#fff}
.card h2{font-size:11.5px;font-weight:700;text-align:center;padding-top:14px}
.card hr{border:none;border-top:1px solid rgba(255,255,255,.35);margin:12px 20px 0}
.card-blue{left:60px;background:linear-gradient(#22a3e0,#1a86cc)}
.card-teal{left:294px;background:linear-gradient(#22b2a4,#178f7a)}
.card-green{left:528px;background:linear-gradient(#69a92f,#4a8a1f)}
.crest{left:22px;top:60px;width:66px;height:72px;background:linear-gradient(#2a58a6,#2e8a3c);border-radius:6px 6px 33px 33px}
.card-text{font-size:7.6px;line-height:16.5px}
.footer-note{left:53px;top:1168px;font-size:7.4px;color:#1b6e8a}
.social{top:1162px;width:23px;height:23px}
</style>
</head>
<body>
<div class="abs page"></div>

<header>
  <div class="abs brand"><span class="brand-dot"></span><span class="brand-name">Coastal Bridge Alliance Conference 2015</span></div>
  <p class="abs tagline">The world's best <em>"COASTAL BRIDGE ALLIANCE CONFERENCE"</em> 2015</p>
  <nav class="abs nav">
    <a class="active" style="width:67px">HOME</a>
    <a style="width:121px">CONFERENCE INFO</a>
    <a style="width:90px">PROGRAMME</a>
    <a style="width:80px">SPEAKERS</a>
    <a style="width:102px">PRESENTATIONS</a>
    <a style="width:121px">ABOUT 10TH CONFEENCE</a>
    <a style="width:126px;border:none">PHOTO GALLERY</a>
  </nav>
</header>

<section>
  <div class="abs slider" role="img" aria-label="Speaker at a podium facing a large conference audience"></div>
  <h1 class="abs slide-title">HEALTH FINANCE INITIATIVE CONFERENCE</h1>
  <p class="abs slide-by">By,<br>Dr. Alan Morrow,<br>Coastal Head</p>
  <div class="abs arrow" style="left:54px"><svg width="10" height="12" viewBox="0 0 10 12"><path d="M8 1 3 6l5 5" fill="none" stroke="#333" stroke-width="2.5"/></svg></div>
  <div class="abs arrow" style="left:731px"><svg width="10" height="12" viewBox="0 0 10 12"><path d="M2 1l5 5-5 5" fill="none" stroke="#333" stroke-width="2.5"/></svg></div>
</section>

<main>
  <h2 class="abs welcome">Welcome to <span>Our 10th Conference</span></h2>
  <p class="abs intro">Donec odio. Quisque volutpat mattis eros. Nullam malesuada erat ut turpis. Suspendisse urna nibh, viverra non, semper suscipit, posuere a, pede. Donec nec justo eget felis facilisis fermentum. Aliquam porttitor mauris sit amet orci. Aenean dignissim pellentesque felis.</p>
  <div class="abs tabs"><span class="on">HEALTH</span><span>FITNESS</span><span>FINANCING INITIATIVE</span><span>INSURANCE</span><span>DISEASE</span></div>

  <div class="abs event-photo" style="top:574px;background:linear-gradient(135deg,#8a6a5a,#d8d0c8 60%,#eee)" role="img" aria-label="Reception room with tables and microphones"></div>
  <article class="abs event" style="top:571px">
    <h3>Welcome Cocktail Reception</h3>
    <p>Sponsored by the National Assurance Board of Port Verde Lorem ipsum dolor sit amet, consectetuer adipiscing elit. Donec</p>
    <div class="meta"><span><i></i>4 JUNE, 2015</span><span><i class="clock"></i>6.00P - 8.00P</span></div>
  </article>

  <div class="abs event-photo" style="top:700px;background:linear-gradient(160deg,#c89a50,#6a4a2a 55%,#3a2a1e)" role="img" aria-label="Audience seated before a presentation screen"></div>
  <article class="abs event" style="top:697px">
    <h3>Soca Walk Fitness Morning</h3>
    <p>Sponsored by the National Assurance Board of Port Verde Lorem ipsum dolor sit amet, consectetuer adipiscing elit. Donec</p>
    <div class="meta"><span><i></i>4 JUNE, 2015</span><span><i class="clock"></i>6.00P - 8.00P</span></div>
  </article>

  <div class="abs event-photo" style="top:826px;background:linear-gradient(180deg,#3a2a24,#2a5aa8 25%,#5a3a2a 50%,#9a6a4a)" role="img" aria-label="Conference hall audience facing a stage screen"></div>
  <article class="abs event" style="top:823px">
    <h3>Island Tour and Shopping</h3>
    <p>Sponsored by the National Assurance Board of Port Verde Lorem ipsum dolor sit amet, consectetuer adipiscing elit. Donec</p>
    <div class="meta"><span><i></i>4 JUNE, 2015</span><span><i class="clock"></i>6.00P - 8.00P</span></div>
  </article>

  <div class="abs pager"><span class="on">1</span><span>2</span><span>&#8594;</span></div>
</main>

<aside>
  <div class="abs promo"><div class="promo-head">Health Finance Initiative</div></div>
  <div class="abs promo-card">
    <h4>PRIOR EVENT</h4>
    <div class="badge" role="img" aria-label="Partner badge"></div>
    <p>Lorem ipsum is simply dummy and is used for the further Lorem is simply dummy</p>
  </div>
  <svg class="abs" style="left:576px;top:462px" width="22" height="30" viewBox="0 0 22 30"><circle cx="12" cy="9" r="8" fill="#e5202a"/><path d="M10 15 4 28" stroke="#888" stroke-width="2"/></svg>
  <div class="abs promo-foot"><b>Welcome to 10th conference</b><span>Click Here</span></div>

  <div class="abs weather">
    <div class="weather-head">WEATHER</div>
    <div class="weather-body"><b>MONTEGO BAY</b>Humidity: 78%<br>Wind: SSE at 6 mph<br>Temp: 78%<br>Detail: Mild &amp; Pleasant</div>
  </div>
  <p class="abs temp">77° F</p>
  <svg class="abs" style="left:636px;top:818px" width="76" height="78" viewBox="0 0 76 78"><circle cx="46" cy="34" r="24" fill="#f0a000"/><circle cx="46" cy="34" r="19" fill="#ffd21a"/><ellipse cx="36" cy="62" rx="32" ry="12" fill="#fff" stroke="#4a8ad0" stroke-width="2"/><circle cx="28" cy="52" r="11" fill="#fff" stroke="#4a8ad0" stroke-width="2"/><circle cx="46" cy="54" r="10" fill="#fff"/><ellipse cx="36" cy="62" rx="30" ry="10" fill="#fff"/></svg>
</aside>

<footer>
  <section class="abs card card-blue">
    <h2>SPONSERS</h2><hr>
    <div class="abs crest" role="img" aria-label="Sponsor crest"></div>
    <div class="abs card-text" style="left:100px;top:60px;width:125px"><b style="color:#d8f0ff">WELLNESS UNION</b><br>Lorem ipsum is simply dummy for ever text in the worspress theme.</div>
  </section>
  <section class="abs card card-teal">
    <h2>VENUE</h2><hr>
    <div class="card-text" style="text-align:center;padding-top:4px"><b style="color:#d8fff6;font-size:8.6px">CONFERENCE AND ACCOMODATION</b><br>SEABREEZE HALL RESORT &amp; SPA,<br>Lorem Hall, Coral Bay, St. Anne,<br>West Indies</div>
    <div class="card-text" style="display:flex;justify-content:center;gap:16px;margin-top:4px"><span>&#9742; 1-800-000-555-0101</span><span>&#9633; 1-800-000-555-0199</span></div>
  </section>
  <section class="abs card card-green">
    <h2>DISCUSSION</h2><hr>
    <div class="card-text" style="padding:6px 0 0 38px"><b>DAY 1</b><br>Aruba - Dr. Pim van Aalst &nbsp;&nbsp;&nbsp;<u>Click here</u><br>Belize - Dr. Renata Olmos &nbsp;&nbsp;&nbsp;<u>Click here</u><br>Bermuda - Mr. Dorian Blake &nbsp;&nbsp;&nbsp;<u>Click here</u><br><i><u>MORE INFO</u></i></div>
  </section>
  <p class="abs footer-note">10th Coastal Bridge Alliance Conference 2015</p>
  <div class="abs social" style="left:676px;background:#2a5a8a" aria-label="Social link"></div>
  <div class="abs social" style="left:707px;background:#d06a2a" aria-label="Social link"></div>
  <div class="abs social" style="left:737px;background:#2aa0d8" aria-label="Social link"></div>
</footer>
</body>
</html>
```